Zielgruppe
Ich zeige Frauen 35+ wie sie ihren Traummann finden können, ohne im Internet nach ihm zu suchen. Meine Zielgruppe sind meist Frauen, die schon lange Single sind und doch voller Sehnsucht nach einem Partner. Diese Frauen haben oft negative Erfolgsverhinderer-Glaubenssätze ('In meinem Alter gibt es keine guten Männer mehr', 'Ich bin zu dick - Männer wollen schlanke Frauen'...). Ich zeige diesen Frauen, wie sie durch eine andere Einstellung in kurzer Zeit ihren Herzenspartner ins Leben ziehen können.
Aufgabenstellung
Die Menschen, die dieses Buch lesen, sind normalerweise weiblich und mindestens 35 Jahre alt, eher älter. Das Cover sollte also Frauen ansprechen, die sich ihren Traummann wünschen und darf gerne auch 'weibliche' Farbtöne wie rot und rosa, pink etc. enthalten (das sind auch 'meine' Business-Farben). Es ist aber nur eine Idee von mir, keine Vorgabe. Ich bin offen für alles.

```html
<!DOCTYPE html>
<html lang="de">
<head>
<meta charset="utf-8">
<title>Wer loslässt dem kommt die Liebe – Buchcover</title>
<link href="https://fonts.googleapis.com/css2?family=Fondamento:ital@0;1&family=Mulish:wght@500&display=swap" rel="stylesheet">
<style>
  :root {
    --paper: #eeeff1;
    --crimson: #c80d2e;
    --heart-red: #d82a3e;
    --heart-pink: #da0f6a;
    --ink: #1a1a1a;
    --white: #ffffff;
    --denim: #36598a;
    --cream: #eadfcf;
  }
  html, body {
    margin: 0;
    padding: 0;
    overflow: hidden;
  }
  .cover {
    position: relative;
    width: 800px;
    height: 1200px;
    overflow: hidden;
    background: radial-gradient(ellipse at 50% 30%, #f6f6f8 0%, var(--paper) 70%, #e6e7ea 100%);
  }
  .author {
    position: absolute;
    top: 44px;
    left: 0;
    width: 800px;
    margin: 0;
    text-align: center;
    font-family: "Mulish", sans-serif;
    font-weight: 500;
    font-size: 38px;
    letter-spacing: 7px;
    color: var(--ink);
  }
  .title {
    position: absolute;
    top: 126px;
    left: 0;
    width: 800px;
    margin: 0;
    text-align: center;
    font-family: "Fondamento", cursive;
    font-weight: 400;
    font-size: 146px;
    line-height: 124px;
    color: var(--crimson);
  }
  .title span { display: block; }
  .couple-photo {
    position: absolute;
    left: 0;
    top: 580px;
    width: 800px;
    height: 620px;
    background:
      linear-gradient(180deg, var(--paper) 0%, rgba(238,239,241,0) 30%),
      linear-gradient(90deg, var(--denim) 0%, #4a6c98 32%, #c9c2b8 55%, var(--cream) 72%, #f1e6d3 100%);
  }
  .heart {
    position: absolute;
    left: 50px;
    top: 520px;
    width: 516px;
    height: 520px;
  }
  .subtitle {
    position: absolute;
    left: 95px;
    top: 645px;
    width: 400px;
    margin: 0;
    text-align: center;
    font-family: "Fondamento", cursive;
    font-style: italic;
    font-size: 42px;
    line-height: 46px;
    color: var(--white);
    transform: rotate(8deg);
    transform-origin: center;
  }
  .subtitle span { display: block; }
</style>
</head>
<body>
  <div class="cover">
    <p class="author">Carla Winterberg-Aulich</p>
    <h1 class="title">
      <span>Wer loslässt</span>
      <span>dem kommt</span>
      <span>die Liebe</span>
    </h1>

    <div class="couple-photo" role="img" aria-label="Foto: lächelnde blonde Frau und ein Mann im Jeanshemd, der sein Gesicht hinter einem großen Papierherz verbirgt"></div>

    <svg class="heart" viewBox="0 0 516 520" aria-hidden="true">
      <path d="M258 140 C225 60 150 5 80 20 C20 35 0 110 20 190 C50 300 180 420 270 515 C340 420 470 330 505 230 C530 150 500 75 420 62 C350 52 290 85 258 140 Z" fill="var(--heart-red)"/>
      <path d="M260 178 C232 110 168 70 115 80 C68 90 52 150 68 210 C95 300 195 395 268 468 C328 390 430 315 458 235 C478 172 455 118 395 110 C340 104 290 130 260 178 Z" fill="var(--heart-pink)"/>
    </svg>

    <p class="subtitle">
      <span>Wieso du</span>
      <span>endlich loslassen</span>
      <span>darfst, um den</span>
      <span>Richtigen</span>
      <span>anzuziehen</span>
    </p>
  </div>
</body>
</html>
```